Gentle Harbor Label

We need labels for a new brewery called "Gentle Harbor":

We need one label, that we can slightly change to suit the style of liquid. So far the beers are:
- XPA
- Pale ALe
- IPA
- Black Ale

We want creative, fun labels, nothing traditional. but appropriate to suit all international markets.

Design was promoted in LOGO & not in Design, so we got a lot of logo's but very little designs for bottles/cans.

Gentle Harbor Brewing

```html
<!DOCTYPE html>
<html lang="en">
<head>
<meta charset="utf-8">
<title>Gentle Harbor Label – Beer Range</title>
<link rel="stylesheet" href="https://fonts.googleapis.com/css2?family=Pirata+One&display=swap">
<style>
  :root {
    --teal: #4dbdc9;
    --teal-deep: #1f8d97;
    --teal-light: #9fe0e6;
    --red: #e94356;
    --red-deep: #c11f3a;
    --red-light: #f7a3ad;
    --orange: #e85d14;
    --orange-deep: #b73d08;
    --orange-light: #f6a777;
    --yellow: #f2d235;
    --yellow-deep: #d3a80e;
    --yellow-light: #f9e98e;
    --ink: #2c2833;
    --violet: #574c9c;
    --white: #ffffff;
    --badge-ink: #3b2e2c;
  }
  * { box-sizing: border-box; margin: 0; padding: 0; }
  html, body { width: 1080px; height: 1200px; overflow: hidden; background: var(--white); }
  .range {
    width: 1080px; height: 1200px;
    display: grid;
    grid-template-columns: repeat(4, 270px);
    grid-template-rows: 598px 602px;
    font-family: "Pirata One", "Times New Roman", serif;
  }
  .label { position: relative; overflow: hidden; background: var(--bg); }
  .label--teal   { --bg: var(--teal);   --deep: var(--teal-deep);   --light: var(--teal-light); }
  .label--red    { --bg: var(--red);    --deep: var(--red-deep);    --light: var(--red-light); }
  .label--orange { --bg: var(--orange); --deep: var(--orange-deep); --light: var(--orange-light); }
  .label--yellow { --bg: var(--yellow); --deep: var(--yellow-deep); --light: var(--yellow-light); }

  .artwork {
    position: absolute; left: 0; right: 4px;
    border-radius: 34px 40px 28px 36px;
    background: linear-gradient(155deg,
      var(--deep) 0%, var(--ink) 22%, var(--bg) 40%,
      var(--violet) 58%, var(--light) 74%, var(--ink) 100%);
  }
  .label--front .artwork { top: 111px; height: 374px; }
  .label--back  .artwork { top: 97px;  height: 378px; }

  .style-name {
    position: absolute; left: 0; right: 0; text-align: center;
    color: var(--white); font-weight: 400; line-height: 1; letter-spacing: -1px;
  }
  .label--front .style-name { top: 486px; font-size: 68px; }
  .label--back  .style-name { top: 34px;  font-size: 50px; }

  .brand-badge {
    position: absolute; left: 50%; transform: translateX(-50%);
    background: var(--bg);
    display: flex; flex-direction: column; align-items: center; justify-content: center;
    text-align: center; line-height: .95;
  }
  .label--front .brand-badge {
    top: 200px; width: 138px; height: 168px;
    border-radius: 69px 69px 22px 22px;
    color: var(--white);
    box-shadow: 0 2px 6px rgba(0,0,0,.25);
  }
  .label--back .brand-badge {
    top: 370px; width: 154px; height: 108px;
    border-radius: 77px 77px 0 0;
    color: var(--badge-ink);
    padding-top: 18px;
    box-shadow: 0 2px 5px rgba(0,0,0,.2);
  }
  .brand-name { font-size: 34px; }
  .brand-sub { font-size: 13px; letter-spacing: 2px; margin-top: 6px; }
  .label--back .brand-name { font-size: 27px; }
  .label--back .brand-sub { font-size: 12px; margin-top: 4px; }
</style>
</head>
<body>
<main class="range">
  <section class="label label--front label--teal">
    <div class="artwork" role="img" aria-label="Dense doodle illustration of playful cartoon monsters in teal, purple and black"></div>
    <div class="brand-badge"><span class="brand-name">Gentle<br>Harbor</span><span class="brand-sub">Brewing</span></div>
    <h2 class="style-name">XPA</h2>
  </section>
  <section class="label label--front label--red">
    <div class="artwork" role="img" aria-label="Dense doodle illustration of playful cartoon monsters in red, purple and black"></div>
    <div class="brand-badge"><span class="brand-name">Gentle<br>Harbor</span><span class="brand-sub">Brewing</span></div>
    <h2 class="style-name">Pale ALe</h2>
  </section>
  <section class="label label--front label--orange">
    <div class="artwork" role="img" aria-label="Dense doodle illustration of playful cartoon monsters in orange, purple and black"></div>
    <div class="brand-badge"><span class="brand-name">Gentle<br>Harbor</span><span class="brand-sub">Brewing</span></div>
    <h2 class="style-name">IPA</h2>
  </section>
  <section class="label label--front label--yellow">
    <div class="artwork" role="img" aria-label="Dense doodle illustration of playful cartoon monsters in yellow, purple and black"></div>
    <div class="brand-badge"><span class="brand-name">Gentle<br>Harbor</span><span class="brand-sub">Brewing</span></div>
    <h2 class="style-name">Black Ale</h2>
  </section>

  <section class="label label--back label--orange">
    <h2 class="style-name">XPA</h2>
    <div class="artwork" role="img" aria-label="Doodle illustration of cartoon monsters and creatures in orange, purple and black"></div>
    <div class="brand-badge"><span class="brand-name">Gentle Harbor</span><span class="brand-sub">Brewing</span></div>
  </section>
  <section class="label label--back label--yellow">
    <h2 class="style-name">Pale Ale</h2>
    <div class="artwork" role="img" aria-label="Doodle illustration of cartoon monsters and creatures in yellow, purple and black"></div>
    <div class="brand-badge"><span class="brand-name">Gentle Harbor</span><span class="brand-sub">Brewing</span></div>
  </section>
  <section class="label label--back label--red">
    <h2 class="style-name">Black Ale</h2>
    <div class="artwork" role="img" aria-label="Doodle illustration of cartoon monsters and creatures in red, purple and black"></div>
    <div class="brand-badge"><span class="brand-name">Gentle Harbor</span><span class="brand-sub">Brewing</span></div>
  </section>
  <section class="label label--back label--teal">
    <h2 class="style-name">IPA</h2>
    <div class="artwork" role="img" aria-label="Doodle illustration of cartoon monsters and creatures in teal, purple and black"></div>
    <div class="brand-badge"><span class="brand-name">Gentle Harbor</span><span class="brand-sub">Brewing</span></div>
  </section>
</main>
</body>
</html>
```